2 Page Business Flyer for Finance Business

Need a two page flyer created for a finance business. Lots of text and needs to fit on two pages.

Corporate business/banking look and feel. Not too many large images. Lots of white space, clean design. Attached is color palette and the text contents of the flyer.

```html
<!DOCTYPE html>
<html lang="en">
<head>
<meta charset="utf-8">
<title>Vanilla Options – Two Page Flyer</title>
<link href="https://fonts.googleapis.com/css2?family=Source+Sans+3:wght@400;600&display=swap" rel="stylesheet">
<style>
:root{
  --navy:#1f1d3a;
  --red:#d94e41;
  --gold:#e2c07e;
  --gold-soft:#dcc592;
  --sand:#dcc38e;
  --sand-light:#ecdcbb;
  --violet:#46466f;
  --violet-band:#5b5a86;
  --backdrop:#e4e4e4;
}
*{margin:0;padding:0;box-sizing:border-box}
html,body{width:1200px;height:941px;overflow:hidden;background:var(--backdrop)}
body{position:relative;font-family:"Source Sans 3",sans-serif}
.page{position:absolute;top:73px;width:703px;height:994px;transform:scale(0.8);transform-origin:0 0;overflow:hidden;background:var(--navy)}
.page--left{left:28px}
.page--right{left:613px}
.shapes{position:absolute;inset:0;width:703px;height:994px}
.abs{position:absolute}
.body-copy{font-size:11px;line-height:14.2px;color:var(--gold-soft)}
.body-copy p+p{margin-top:14px}
.title-banner{left:31px;top:120px;color:#fff;font-size:23px;line-height:25px;width:350px}
.title-banner span{display:block}
.title-banner span:last-child{text-align:right}
.bullets{list-style:none;font-size:11px;line-height:14px;color:#eee}
.bullets li{position:relative;padding-left:11px;margin-bottom:9.5px}
.bullets li::before{content:"•";position:absolute;left:0}
.panel-heading{font-size:20px;color:var(--navy);letter-spacing:.2px}
.dash-list{list-style:none;font-size:11px;line-height:14.2px;color:var(--navy)}
.dash-list li{position:relative;padding-left:10px}
.dash-list li::before{content:"-";position:absolute;left:0}
.risks-label{left:34px;top:38px;color:var(--red);font-size:36px;line-height:40px}
.risks-note{left:177px;top:37px;color:var(--sand-light);font-size:18px;line-height:19px;font-weight:600;width:480px}
.why-heading{left:60px;top:296px;color:var(--gold);font-size:26px;line-height:34px;font-weight:600}
.why-lead{left:60px;top:374px;width:270px;color:var(--gold);font-size:18.5px;line-height:22.7px}
.price-list{list-style:none;font-size:11.5px;line-height:16.4px;color:var(--navy)}
.price-list li{position:relative;padding-left:10px;margin-bottom:17px}
.price-list li::before{content:"•";position:absolute;left:0}
</style>
</head>
<body>

<!-- Page one -->
<section class="page page--left">
  <svg class="shapes" viewBox="0 0 703 994" aria-hidden="false">
    <defs>
      <linearGradient id="skyline" x1="0" y1="0" x2="1" y2="1">
        <stop offset="0" stop-color="#7f9fc6"/>
        <stop offset=".5" stop-color="#3c5a86"/>
        <stop offset="1" stop-color="#22304d"/>
      </linearGradient>
    </defs>
    <rect x="0" y="0" width="703" height="315" fill="url(#skyline)" role="img" aria-label="Photograph of glass office towers against a cloudy blue sky"/>
    <polygon points="0,300 372,300 703,100 703,150 382,313 0,313" fill="var(--red)"/>
    <polygon points="0,313 382,313 703,150 703,994 0,994" fill="var(--navy)"/>
    <polygon points="0,114 413,114 398,177 0,177" fill="var(--red)"/>
    <polygon points="0,512 370,512 350,634 0,634" fill="var(--violet)"/>
    <polygon points="0,785 400,785 373,967 0,967" fill="var(--sand-light)"/>
    <polygon points="400,785 703,785 703,967 373,967" fill="var(--sand)"/>
  </svg>

  <h1 class="abs title-banner"><span>HOW DOES A VANILLA OPTION</span><span>CONTRACT WORK?</span></h1>

  <div class="abs body-copy" style="left:60px;top:347px;width:305px">
    <p>The buyer of a vanilla option receives protection against an adverse movement in the exchange rate while allowing full participation in a beneficial move. At no time is the buyer of a Vanilla Option obligated to exercise the Option and transact the currencies, therefore providing flexibility in cases where the requirement to purchase foreign currency is not certain.</p>
    <p>A buyer of vanilla options is required to pay a premium (like an insurance premium) for the right, but not the obligation, to exchange currency at a predetermined rate on a predetermined date.</p>
  </div>

  <ul class="abs bullets" style="left:60px;top:522px;width:290px">
    <li>Set a protection rate which will be your worst-case scenario at expiry</li>
    <li>Determine the amount of currency you wish to protect</li>
    <li>Choose an expiry date for the contract</li>
    <li>Calculate the premium you are required to pay</li>
  </ul>

  <div class="abs body-copy" style="left:60px;top:652px;width:300px">
    <p>Let’s look at an example: You are in importer.<br>Your construction company has bid on a project that if successful, will require you to import materials from the United States to use in construction. You have used todays pricing of materials in calculating your bid and want to protect against an adverse move in the US dollar exchange rate from eroding your margin if your bid is chosen for the project.</p>
  </div>

  <div class="abs body-copy" style="left:390px;top:347px;width:255px">
    <p>You choose to buy a Vanilla Call which will protect you from a rise in the USD/CAD exchange rate above your protection rate. You choose to buy protection on $500,000 USD, with a protection rate (strike rate) of 1.3300 expiring 3 months from now. You are required to pay a premium which in this case is calculated to be 1.8%, or 11,970 CAD.</p>
    <p>Your bid is successful: If the exchange rate is below your protection rate at expiration, you have no obligation relating to the vanilla call and you are free to buy USD at the cheaper spot rate. If the exchange rate is above your protection rate, your have the right to purchase your USD at the protection rate, and thereby claiming your insurance policy.</p>
    <p>Your bid is not successful: You have no obligation relating to the vanilla option however, if at expiry the exchange rate is above the protection rate, you may exercise your right to buy USD at the lower rate and simultaneous sell USD back at the prevailing spot rate, thereby recouping some or all of the premium paid to buy the option. Alternatively, if you find out your bid was not successful with time still left until expiration, you may sell your option back into the market in the case that it still has residual value, which will depend on various market factors.</p>
  </div>

  <h2 class="abs panel-heading" style="left:60px;top:800px">CHARACTERISTICS</h2>
  <ul class="abs dash-list" style="left:60px;top:839px;width:280px">
    <li>You are looking for a straight-forward hedging solution</li>
    <li>You want to receive full benefit from an appreciation of the currency you are exposed to</li>
    <li>You are comfortable receiving protection at the strike rate of the option</li>
    <li>You are willing to pay the non-refundable premium</li>
  </ul>

  <h2 class="abs panel-heading" style="left:389px;top:800px">ADVANTAGES</h2>
  <ul class="abs dash-list" style="left:389px;top:839px;width:255px">
    <li>You hedge your foreign currency exposure at a predefined hedge rate</li>
    <li>You can choose the hedge rate that suits your budget requirements</li>
    <li>Provides the ability to fully participate in a favourable exchange rate move</li>
    <li>You can choose from most major currency pairs to meet your needs</li>
  </ul>
</section>

<!-- Page two -->
<section class="page page--right">
  <svg class="shapes" viewBox="0 0 703 994">
    <defs>
      <linearGradient id="desk" x1="0" y1="0" x2="1" y2="1">
        <stop offset="0" stop-color="#a7896a"/>
        <stop offset=".55" stop-color="#6e523c"/>
        <stop offset="1" stop-color="#3b2b22"/>
      </linearGradient>
      <linearGradient id="portrait" x1="0" y1="0" x2="1" y2="1">
        <stop offset="0" stop-color="#8ea26a"/>
        <stop offset=".6" stop-color="#3e7476"/>
        <stop offset="1" stop-color="#23484d"/>
      </linearGradient>
    </defs>
    <rect x="0" y="0" width="703" height="313" fill="url(#desk)" role="img" aria-label="Photograph of hands signing a document on a clipboard at a wooden desk"/>
    <polygon points="0,26 703,26 703,89 0,89" fill="var(--violet-band)"/>
    <polygon points="0,26 155,26 140,89 0,89" fill="var(--navy)"/>
    <polygon points="0,100 330,300 703,300 703,313 325,313 0,145" fill="var(--red)"/>
    <polygon points="0,145 325,313 703,313 703,994 0,994" fill="var(--navy)"/>
    <polygon points="354,490 703,490 703,994 306,994" fill="var(--sand)"/>
    <polygon points="0,714 320,849 306,994 0,994" fill="url(#portrait)" role="img" aria-label="Photograph of a smiling woman outdoors holding a smartphone"/>
  </svg>

  <div class="abs risks-label">RISKS</div>
  <div class="abs risks-note">Premium paid is non-refundable and remains your only obligation when buying vanilla options</div>

  <h2 class="abs why-heading">WHY USE<br>VANILLA OPTIONS?</h2>
  <p class="abs why-lead">Vanilla options are often compared to an insurance product. The buyer pays a non-refundable premium for the right, but not the obligation to trade currency in the future at the protection rate of the option. This product allows you to participate in a beneficial move to an unlimited extent, which will be the most advantageous outcome, if the exchange rate moves in your favour enough to more than offset the premium paid for the option.</p>

  <div class="abs body-copy" style="left:380px;top:347px;width:270px;font-size:11.5px;line-height:16.4px">
    <p>What determines the price of a Vanilla Option? The cost of an option is defined by the premium that is required to be paid in order to enter into the contract. Premiums are calculated using the industry standard formulas based upon the Black Scholes model. The most important variables in the option pricing formulas include the following:</p>
  </div>

  <ul class="abs price-list" style="left:380px;top:512px;width:270px">
    <li>The current market Spot Rate.</li>
    <li>Market volatility – the higher the volatility, the higher the premium.</li>
    <li>The Term of the Option – a longer term typically results in a higher premium.</li>
    <li>The Strike Rate – the closer to being ITM the protection rate is, the higher the premium.</li>
    <li style="margin-bottom:33px">The interest rate differential of the two currencies involved.</li>
    <li>Style – European or American, or whether the option can be exercised prior to expiration An option can either a European (meaning that they can only be exercised on the expiry date), or American (meaning that they can be exercised at any time prior to expiration). We normally deals in European options however, we do offer American options under certain circumstances and when specific delivery terms are agreed upon between us and the customer.</li>
  </ul>
</section>

</body>
</html>
```